Card and board game developer website, small e-commerce site

We are designing a website for Spinning Otter Gadget Works. I need a homepage and a typical inside page designed.
The website navigation will be:
Home (where we'll introduce the games and the website)
Our Games (drops open into the two games)
Griffins of Morvandale
Quintessa
Order Now
About Us
Contact
The header of the website will include the logo, the navigation and a link to a facebook page. The header will also include a cart icon and a link to My Account.
Then on the homepage I suggest we include a row for each game:
Griffins of Morvandale
This row will include a photo (or maybe a series of photos that animate into each other) and quick info about the game plus two buttons: Info and Photos (which will go to the detail page with the photo gallery), and Order Now (which will take you to the product for ordering).
Quintessa
Your footer will contain a copyright note, plus links to:
Terms and conditions
Shipping and returns
FAQ
Contact
Account login
NOTE: the logo is the orange mokey. I've uploaded a brief with more information. The current website that we are redesigning is here https://www.spinningottergadget.example/
Please send me any questions that you have.
People interested in fun card and board games at home.
2 page

```html
<!DOCTYPE html>
<html lang="en">
<head>
<meta charset="utf-8">
<title>Spinning Otter Gadget Works – Home</title>
<link rel="stylesheet" href="https://fonts.googleapis.com/css2?family=Poppins:wght@400;500;600;700;800;900&display=swap">
<style>
  :root{
    --orange:#f28322;
    --ink:#111111;
    --white:#ffffff;
    --mist:#ebebed;
    --field:#e6e6e6;
    --photo-grey:#c8c7ce;
    --black:#000000;
  }
  *{box-sizing:border-box;margin:0;padding:0}
  html,body{width:1200px;height:3349px;overflow:hidden}
  body{position:relative;font-family:'Poppins',sans-serif;color:var(--ink);background:var(--white)}
  .abs{position:absolute}

  /* header */
  .site-header{position:absolute;left:0;top:0;width:1200px;height:78px;background:var(--white);z-index:3}
  .nav-bar{position:absolute;left:312px;top:49px;width:784px;height:60px;background:var(--orange);
    clip-path:polygon(0 0,100% 0,100% 100%,14px 100%);z-index:4;display:flex;align-items:center;padding-left:50px}
  .nav-bar a{color:var(--white);text-decoration:none;font-weight:600;font-size:15px;margin-right:29px;display:flex;align-items:center;gap:4px;white-space:nowrap}
  .nav-icon{width:31px;height:31px;border:1.5px solid var(--white);border-radius:50%;margin-right:10px;display:flex;align-items:center;justify-content:center;flex:none}
  .nav-icon.cart{background:var(--white)}
  .account-btn{border:2px solid var(--white);padding:6px 11px;margin-left:20px;margin-right:0!important;font-size:14px!important}
  .logo-badge{position:absolute;left:91px;top:7px;width:156px;height:156px;border-radius:50%;background:var(--white);z-index:5;
    display:flex;align-items:center;justify-content:center;text-align:center;padding:22px;
    color:var(--orange);font-weight:700;font-size:16px;line-height:1.15}

  /* hero */
  .hero{position:absolute;left:0;top:78px;width:1200px;height:602px;
    background:radial-gradient(circle at 30% 40%,#6f8a3a 0,#4b6b2e 25%,transparent 55%),
               radial-gradient(circle at 80% 70%,#b59a3b 0,#7d7c34 30%,transparent 60%),
               linear-gradient(135deg,#5a7334,#8c8a3e 45%,#556b31 70%,#9a8b45)}
  .hero-copy{position:absolute;left:0;width:1200px;text-align:center;color:var(--white);text-shadow:3px 3px 0 #000}
  .hero-kicker{top:205px;font-weight:800;font-size:20px}
  .hero-title{top:252px;font-weight:900;font-size:62px;line-height:70px;text-transform:uppercase}

  .section-title{font-weight:900;color:var(--orange);text-transform:uppercase;font-size:33px;line-height:40px;
    text-shadow:2px 2px 0 #5a2a00}

  .btn{position:absolute;display:flex;align-items:center;justify-content:center;font-weight:500;font-size:17px;text-decoration:none}
  .btn-solid{background:var(--orange);color:var(--white)}
  .btn-outline{background:var(--white);color:var(--ink);border:2px solid var(--ink)}

  /* game rows */
  .game-photo{position:absolute;background:var(--photo-grey)}
  .game-copy{font-size:14.5px;line-height:26.5px;letter-spacing:-0.1px}
  .copy-stack{position:absolute;display:flex;flex-direction:column}
  .copy-stack .launch-note{font-weight:700;font-size:15px;margin-top:9px}
  .stat-circle{position:absolute;width:76px;height:76px;border-radius:50%;background:var(--white);
    box-shadow:0 2px 10px rgba(0,0,0,.14);display:flex;align-items:center;justify-content:center}
  .stat-text{position:absolute;font-weight:500;font-size:16.5px}
  .band-mist{position:absolute;left:0;top:1448px;width:1200px;height:599px;background:var(--mist)}
  .launch-badge{position:absolute;left:575px;top:1540px;width:86px;height:86px;border-radius:50%;background:var(--orange);
    border:3px solid var(--orange);box-shadow:inset 0 0 0 2px var(--white);color:var(--white);font-size:10px;font-weight:600;
    line-height:17px;display:flex;align-items:center;justify-content:center;text-align:center;z-index:2}

  /* about */
  .band-dark{position:absolute;left:0;top:2047px;width:1200px;height:603px;background:var(--black)}
  .about-art{position:absolute;left:0;top:2076px;width:547px;height:574px;
    background:radial-gradient(ellipse at 45% 55%,#6c7257 0,#3c4a2b 40%,#14200f 80%)}
  .about-title{position:absolute;left:636px;top:2160px;color:var(--white);font-weight:800;font-size:34px;line-height:41px;text-transform:uppercase}
  .about-sub{position:absolute;left:640px;top:2258px;color:var(--white);font-weight:600;font-size:19px}
  .about-copy{position:absolute;left:640px;top:2298px;width:485px;color:var(--white);font-size:14.5px;line-height:30px;letter-spacing:-0.1px}

  /* contact */
  .field{position:absolute;background:var(--field);font-weight:500;font-size:17px;padding-left:13px;display:flex;align-items:center}
  .field.message{align-items:flex-start;padding-top:12px}

  /* footer */
  .site-footer{position:absolute;left:0;top:3111px;width:1200px;height:238px;background:var(--mist)}
  .footer-logo{position:absolute;left:106px;top:58px;width:210px;display:flex;align-items:center;gap:12px;color:var(--orange);font-weight:700;font-size:18px;line-height:22px}
  .footer-logo .dot{width:46px;height:46px;border-radius:50%;background:var(--orange);flex:none}
  .footer-links{position:absolute;left:424px;top:78px;font-size:15px;display:flex;gap:12px;color:var(--ink);white-space:nowrap}
  .footer-links a{color:var(--ink);text-decoration:none}
  .footer-rule{position:absolute;left:424px;top:130px;width:672px;height:1px;background:#333}
  .copyright{position:absolute;left:429px;top:160px;font-size:12px}
</style>
</head>
<body>

<header class="site-header"></header>
<div class="logo-badge">Spinning Otter Gadget Works</div>
<nav class="nav-bar">
  <a href="#">Home</a>
  <a href="#">Our Games
    <svg width="10" height="7" viewBox="0 0 10 7"><path d="M1 1l4 4 4-4" fill="none" stroke="#fff" stroke-width="1.6"/></svg></a>
  <a href="#">Order Now</a>
  <a href="#">About Us</a>
  <a href="#">Contact</a>
  <span class="nav-icon" aria-label="Social page"></span>
  <span class="nav-icon cart" aria-label="Cart">
    <svg width="15" height="13" viewBox="0 0 15 13"><path d="M0 1h3l2 7h7l2-5H4" fill="none" stroke="#111" stroke-width="1.8"/><circle cx="6" cy="11" r="1.3" fill="#111"/><circle cx="11" cy="11" r="1.3" fill="#111"/></svg>
  </span>
  <a href="#" class="account-btn">My Account</a>
</nav>

<section class="hero" role="img" aria-label="Painted overhead fantasy map with forests, rivers and fields">
  <div class="hero-copy hero-kicker">WELCOME TO</div>
  <h1 class="hero-copy hero-title">Spinning Otter<br>Gadget Works</h1>
</section>

<!-- Griffins of Morvandale -->
<div class="game-photo" style="left:104px;top:746px;width:495px;height:493px;background:linear-gradient(160deg,#cfced4,#c3c2c9)" role="img" aria-label="Griffins of Morvandale game box"></div>
<h2 class="abs section-title" style="left:637px;top:756px">Griffins of<br>Morvandale</h2>
<p class="abs game-copy" style="left:638px;top:855px;width:430px">Welcome to The Griffins Of Morvandale, the first board game where every player is a GRIFFIN</p>
<p class="abs game-copy" style="left:640px;top:917px;width:460px">Conquer territory and build your empire.&nbsp; Plunder castles and collect a huge hoard of gold. Rescue relatively attractive royalty or maybe eat them.&nbsp; Who knows?&nbsp; All we know is that everyone's a winner when the pizza's delivered!**</p>
<div class="stat-circle" style="left:639px;top:1049px">
  <svg width="44" height="36" viewBox="0 0 44 36" fill="#f28322">
    <circle cx="22" cy="8" r="6"/><circle cx="9" cy="12" r="4.5"/><circle cx="35" cy="12" r="4.5"/>
    <path d="M12 34c0-9 4-14 10-14s10 5 10 14z"/><path d="M1 32c0-7 3-11 8-11 2 0 3 .5 4 1.5-2 3-3 6-3 9.5z"/><path d="M43 32c0-7-3-11-8-11-2 0-3 .5-4 1.5 2 3 3 6 3 9.5z"/>
  </svg>
</div>
<div class="stat-text" style="left:732px;top:1075px">2 - 6 players *</div>
<div class="stat-circle" style="left:639px;top:1146px">
  <svg width="50" height="50" viewBox="0 0 50 50"><circle cx="25" cy="25" r="21" fill="none" stroke="#f28322" stroke-width="3"/><path d="M25 12v14l8 6" fill="none" stroke="#f28322" stroke-width="3" stroke-linecap="round"/></svg>
</div>
<div class="stat-text" style="left:732px;top:1172px">Playtime approximately 1.5 hours.</div>
<p class="abs" style="left:0;width:1200px;top:1273px;text-align:center;font-weight:500;font-size:20px">Game comes with 4 griffin packs.&nbsp; Additional griffin Expansion packs coming soon.</p>
<a class="btn btn-solid" href="#" style="left:438px;top:1323px;width:178px;height:48px">Info and Photos</a>
<a class="btn btn-outline" href="#" style="left:623px;top:1323px;width:139px;height:48px">Order Now</a>

<!-- Quintessa -->
<div class="band-mist"></div>
<h2 class="abs section-title" style="left:104px;top:1583px">Quintessa</h2>
<div class="copy-stack" style="left:104px;top:1638px;width:455px">
  <p class="game-copy">Welcome to Quintessa, a fast paced card game of strategy and chance.&nbsp; Play your element cards (Earth, Air, Fire,Water) and wild cards (Guardian, Balance, Evolution, Genesis) wisely and be the first player to discard all of their cards and declare yourself the master of the elements.</p>
  <p class="launch-note">Coming to Backerfund soon.</p>
</div>
<a class="btn btn-solid" href="#" style="left:104px;top:1828px;width:179px;height:47px">Info and Photos</a>
<a class="btn btn-outline" href="#" style="left:290px;top:1828px;width:138px;height:47px">Order Now</a>
<div class="game-photo" style="left:599px;top:1566px;width:497px;height:366px" role="img" aria-label="Quintessa card deck box"></div>
<div class="launch-badge">Coming to<br>Backerfund<br>soon</div>

<!-- About -->
<div class="band-dark"></div>
<div class="about-art" role="img" aria-label="Painted creature standing in a misty forest"></div>
<h2 class="about-title">About Spinning<br>Otter Gadget Works</h2>
<p class="about-sub">They say do what you love...</p>
<p class="about-copy">At Spinning Otter Gadget Works we love to dream big dreams and bring those dreams to life. We create games to entertain and engage the people that play them; games that invite and inspire players to add a bit of themselves to each game, and how it is played.</p>
<a class="btn btn-solid" href="#" style="left:640px;top:2480px;width:202px;height:49px;font-weight:600">Come play with us.</a>

<!-- Contact -->
<h2 class="abs section-title" style="left:0;width:1200px;text-align:center;top:2738px">Contact Us</h2>
<div class="field" style="left:165px;top:2803px;width:384px;height:53px">Name</div>
<div class="field" style="left:165px;top:2868px;width:384px;height:52px">Phone Number</div>
<div class="field" style="left:165px;top:2932px;width:384px;height:52px">Email</div>
<div class="field message" style="left:558px;top:2803px;width:477px;height:181px">Message</div>
<a class="btn btn-solid" href="#" style="left:542px;top:3002px;width:115px;height:43px;font-weight:600">Submit</a>

<!-- Footer -->
<footer class="site-footer">
  <div class="footer-logo"><span class="dot"></span>Spinning Otter Gadget Works</div>
  <nav class="footer-links">
    <a href="#">Terms and conditions</a><span>|</span>
    <a href="#">Shipping and returns</a><span>|</span>
    <a href="#">FAQ</a><span>|</span>
    <a href="#">Contact</a><span>|</span>
    <a href="#">Account login</a>
  </nav>
  <div class="footer-rule"></div>
  <p class="copyright">©Copyrights 2024 Spinning Otter Gadget Works | All Rights Reserved</p>
</footer>

</body>
</html>
```